Business Card Design for Cybersecurity Company - Quorvent Systems

We need a business card design for our new cybersecurity company, Quorvent. We’re going for a clean, hi tech look that feels modern, premium, and trustworthy. We want a design that really stands out and makes people say WOW when we hand it over!

Quorvent delivers reliable IT support and managed services for small and mid sized businesses. We help companies stay secure, efficient, and connected through proactive monitoring, cybersecurity services, cloud management, and remote support.

Target Market(s)

Designers should target small and mid sized businesses that need dependable cybersecurity and IT support.

Industry/Entity Type

Cybersecurity, Managed Service Provider, IT services

Contact Information for Business Card

Contact information

Requirements
Must have
• The card should look clean, modern, and tech focused, with the Quorvent logo, clear contact info, and strong readability. It needs to feel premium and professional while still keeping a simple layout that fits a cybersecurity and IT brand.
Nice to have
• Nice to have elements include subtle touches that give the card a modern, tech feel, along with a layout that works well in different background styles.
Should not have
• The card should avoid clutter, loud graphics, or anything that takes attention away from the logo and contact details.

```html
<!DOCTYPE html>
<html lang="en">
<head>
<meta charset="utf-8">
<title>Quorvent Systems – Business Card</title>
<link href="https://fonts.googleapis.com/css2?family=Montserrat:wght@400;500;700&display=swap" rel="stylesheet">
<style>
  :root {
    --stage: #2a2a2c;
    --card: #060607;
    --card-edge: #1a1a1d;
    --pattern: #111114;
    --blue: #4f7fe0;
    --violet: #8a5ce0;
    --white: #f2f2f5;
    --muted: #c9c9d2;
  }
  * { margin: 0; padding: 0; box-sizing: border-box; }
  html, body { width: 1200px; height: 875px; overflow: hidden; }
  body {
    background: var(--stage);
    font-family: "Montserrat", sans-serif;
    color: var(--white);
    position: relative;
  }
  .card {
    position: absolute;
    left: 250px;
    width: 700px;
    height: 400px;
    background: var(--card);
    border: 1px solid var(--card-edge);
    border-radius: 22px;
    overflow: hidden;
    box-shadow: 0 18px 40px rgba(0,0,0,.45);
  }
  .card--back { top: 28px; }
  .card--front { top: 447px; }

  /* back */
  .back-pattern {
    position: absolute; inset: 0;
    background: linear-gradient(135deg, var(--pattern), #070708 60%, var(--pattern));
  }
  .back-brand {
    position: absolute; right: 150px; top: 170px;
    display: flex; align-items: center; gap: 14px;
  }
  .brand-mark {
    width: 30px; height: 30px;
    border: 3px solid var(--blue);
    border-radius: 4px;
  }
  .brand-name {
    font-weight: 700; font-size: 34px; color: var(--blue);
    letter-spacing: .5px;
  }

  /* front */
  .front-brand {
    position: absolute; left: 60px; top: 218px;
    display: flex; align-items: center; gap: 14px;
  }
  .front-brand .brand-mark { width: 46px; height: 46px; }
  .brand-words .brand-name { font-size: 40px; line-height: 1; display: block; }
  .brand-tag {
    display: block; margin-top: 6px;
    font-size: 13px; font-weight: 400; letter-spacing: 7px; color: var(--muted);
  }
  .divider {
    position: absolute; left: 372px; top: 70px;
    width: 2px; height: 240px;
    background: linear-gradient(var(--blue), var(--violet));
  }
  .contact { position: absolute; left: 400px; top: 72px; }
  .person-name {
    font-size: 30px; font-weight: 700; color: var(--blue); line-height: 1.1;
  }
  .person-role {
    font-size: 13px; font-weight: 400; color: var(--white); margin-top: 6px;
  }
  .contact-list { list-style: none; margin-top: 26px; }
  .contact-list li {
    display: flex; align-items: center; gap: 12px;
    font-size: 16px; font-weight: 400; margin-bottom: 12px;
  }
  .contact-list svg { width: 16px; height: 16px; fill: var(--violet); flex: none; }
</style>
</head>
<body>

<section class="card card--back" aria-label="Card back">
  <div class="back-pattern" role="img" aria-label="Subtle gloss pattern of repeated hexagonal circuit emblems on black"></div>
  <div class="back-brand">
    <span class="brand-mark"></span>
    <span class="brand-name">Quorvent</span>
  </div>
</section>

<section class="card card--front" aria-label="Card front">
  <div class="front-brand">
    <span class="brand-mark"></span>
    <div class="brand-words">
      <span class="brand-name">Quorvent</span>
      <span class="brand-tag">Systems</span>
    </div>
  </div>

  <div class="divider"></div>

  <div class="contact">
    <h1 class="person-name">Dorian Castell</h1>
    <p class="person-role">Owner | CEO | Quorvent Systems</p>
    <ul class="contact-list">
      <li>
        <svg viewBox="0 0 24 24"><path d="M3 9c0-3 4-5 9-5s9 2 9 5v2h-5V9H8v2H3zM6 12h12l2 8H4z"/></svg>
        (855) 555-0142
      </li>
      <li>
        <svg viewBox="0 0 24 24"><path d="M6.6 10.8a15 15 0 0 0 6.6 6.6l2.2-2.2c.3-.3.7-.4 1-.2 1.1.4 2.3.6 3.6.6.6 0 1 .4 1 1V20c0 .6-.4 1-1 1A17 17 0 0 1 3 4c0-.6.4-1 1-1h3.5c.6 0 1 .4 1 1 0 1.3.2 2.5.6 3.6.1.3 0 .7-.2 1z"/></svg>
        (813) 555-0187
      </li>
      <li>
        <svg viewBox="0 0 24 24"><path d="M2 5h20v14H2zm2 2v.5l8 5 8-5V7l-8 5z"/></svg>
        dorian@quorvent.com
      </li>
      <li>
        <svg viewBox="0 0 24 24"><circle cx="12" cy="12" r="10"/></svg>
        www.quorvent.com
      </li>
    </ul>
  </div>
</section>

</body>
</html>
```